Basic Website for Vending Machine Business

We need a website designed for our vending machine business, Munchotronix, which is located in Ottawa, Canada. We requires a few links to standard sub-pages (About Us, Machines, Request a Machine, Report a Problem, Contact Us, etc.). We want it to be fun and simple. Possibly involve a vending machine in some way - make selections inside the machine the links to sub pages? Just an idea, we are very flexible though...please be creative. Attached are the drafts of our logo, we will provide the official copies of logo in near future. Key for our website is we want it visually appealing and fun, as opposed to formal.
Some slogans you may wish to use:
- Vend. Snack. Smile.
- Shop. Snack. Smile.
Target Market(s)
Small and medium size business owners.
Industry/Entity Type
Business
Look and feel

```html
<!DOCTYPE html>
<html lang="en">
<head>
<meta charset="utf-8">
<title>Munchotronix – Vending Machines</title>
<link href="https://fonts.googleapis.com/css2?family=Raleway:wght@300;400;500&family=Lato:ital,wght@0,400;0,700;0,900;1,400&display=swap" rel="stylesheet">
<style>
:root{
  --maroon:#6b2140;
  --maroon-dark:#561a33;
  --ink:#2b2b2b;
  --text:#444;
  --muted:#8a8a8a;
  --line:#d9d9d9;
  --band:#dcdcdc;
  --footer:#6f6f6f;
  --white:#fff;
  --orange:#f26a1b;
}
*{box-sizing:border-box;margin:0;padding:0}
html,body{width:1200px;height:2500px;overflow:hidden}
body{position:relative;background:var(--white);font-family:'Lato',sans-serif;color:var(--text)}
.abs{position:absolute}

/* header */
.site-header{left:0;top:0;width:1200px;height:72px;background:var(--white)}
.brand{left:122px;top:18px;display:flex;align-items:center;gap:10px}
.brand-mark{width:26px;height:26px;background:var(--maroon)}
.brand-name{font-family:'Lato',sans-serif;font-weight:900;font-size:28px;color:var(--maroon)}
.main-nav{right:122px;top:24px;display:flex;gap:30px;font-size:13px;color:var(--ink)}
.main-nav a{color:inherit;text-decoration:none}
.main-nav a.active{color:var(--maroon)}

/* hero */
.hero{left:0;top:72px;width:1200px;height:523px;
  background:radial-gradient(ellipse at 35% 35%,#5a4a40 0%,#2a2a2a 35%,#111 70%),#111}
.hero-splash-left{left:0;top:72px;width:460px;height:440px;
  background:radial-gradient(ellipse at 20% 30%,#f2f2f2 0%,#cfcfcf 30%,rgba(120,60,20,.8) 55%,rgba(0,0,0,0) 75%)}
.hero-splash-right{left:780px;top:120px;width:420px;height:475px;
  background:radial-gradient(ellipse at 65% 60%,#ffc23a 0%,#f39a1a 35%,rgba(230,110,20,.6) 55%,rgba(0,0,0,0) 75%)}
.hero-caption{left:300px;top:283px;width:600px;height:117px;background:rgba(30,30,30,.82);text-align:center;color:var(--white)}
.hero-caption h1{font-family:'Raleway',sans-serif;font-weight:300;font-size:35px;margin-top:22px;letter-spacing:.5px}
.hero-caption p{font-family:'Raleway',sans-serif;font-size:12px;letter-spacing:5px;margin-top:12px}
.hero-dots{left:575px;top:495px;display:flex;gap:6px}
.hero-dots span{width:13px;height:13px;border-radius:50%;background:var(--orange)}

/* category cards */
.category-card{top:525px;width:300px;height:310px;background:var(--white);border:1px solid var(--line);text-align:center}
.category-card .photo{position:absolute;left:13px;top:13px;width:272px;height:179px}
.category-card h2{position:absolute;left:0;right:0;top:202px;font-family:'Raleway',sans-serif;font-weight:400;font-size:21px;line-height:28px;color:var(--ink)}
.category-shadow{top:835px;width:300px;height:16px;background:radial-gradient(ellipse at 50% 0%,rgba(0,0,0,.55) 0%,rgba(0,0,0,0) 70%)}
.read-more{display:inline-flex;align-items:center;gap:6px;font-size:12px;font-weight:700;color:var(--maroon)}
.read-more svg{width:11px;height:11px}
.category-card .read-more{position:absolute;left:0;right:0;top:278px;justify-content:center}

/* about */
.about-title{left:0;top:888px;width:1200px;text-align:center;font-family:'Raleway',sans-serif;font-weight:400;font-size:42px;color:var(--ink)}
.about-photo{left:197px;top:957px;width:240px;height:240px;border-radius:50%;
  background:radial-gradient(circle at 50% 45%,#c9463a 0%,#7a6b3a 35%,#2a2a2a 75%)}
.about-body{left:532px;top:970px;width:545px}
.about-body h3{font-family:'Lato',sans-serif;font-style:italic;font-weight:400;font-size:21px;color:var(--maroon)}
.about-body p{font-style:italic;font-size:10.5px;line-height:16px;color:#333;margin-top:14px}
.btn{display:inline-flex;align-items:center;gap:8px;background:var(--maroon);color:var(--white);font-weight:700;font-size:13px;border-radius:2px}
.about-body .btn{margin-top:28px;height:47px;padding:0 22px;box-shadow:0 3px 0 var(--maroon-dark)}

/* machines band */
.machines-band{left:0;top:1243px;width:1200px;height:514px;
  background:linear-gradient(90deg,#c8c8c8 0%,#e6e6e6 40%,#e2e2e2 70%,#f0c890 100%)}
.machine-card{top:1302px;width:218px}
.machine-card .photo{width:218px;height:278px;background:var(--white);position:relative}
.machine-card .photo span{position:absolute;left:32px;top:10px;width:154px;height:255px;border-radius:3px}
.machine-card h4{margin-top:14px;font-family:'Lato',sans-serif;font-weight:400;font-size:15px;color:var(--maroon)}
.machine-card p{margin-top:8px;font-size:10px;line-height:14px;color:#222;font-weight:700}
.machine-card .read-more{display:flex;justify-content:flex-end;margin-top:12px}

/* newsletter */
.newsletter{left:100px;top:1803px;width:1000px;height:94px;background:#f0f0f0;box-shadow:0 6px 10px rgba(0,0,0,.15)}
.newsletter h5{position:absolute;left:23px;top:32px;font-family:'Raleway',sans-serif;font-weight:400;font-size:23px;color:var(--maroon)}
.newsletter .field{position:absolute;left:350px;top:24px;width:447px;height:50px;border:1px solid var(--maroon);background:var(--white);font-size:12px;color:#333;padding:17px 15px}
.newsletter .send{position:absolute;left:797px;top:24px;width:96px;height:50px;background:var(--maroon);display:flex;align-items:center;justify-content:center}

/* footer columns */
.col-title{top:1957px;font-family:'Raleway',sans-serif;font-weight:400;font-size:26px;color:var(--ink)}
.contact-list{left:125px;top:2015px;width:300px;font-size:14px;color:#333}
.contact-list li{list-style:none;display:flex;gap:16px;margin-bottom:22px;line-height:20px}
.contact-list svg{flex:none;width:16px;height:16px;margin-top:2px}
.info-list{left:450px;top:2008px;font-size:14px;color:#333}
.info-list li{list-style:none;display:flex;align-items:center;gap:14px;height:26.7px}
.info-list svg{width:13px;height:13px}
.report-form{left:695px;top:2012px;width:380px}
.report-form .input{position:absolute;height:31px;border:1px solid #999;border-radius:3px;font-size:9px;color:#444;padding:9px 9px}
.report-form .submit{position:absolute;left:0;top:148px;width:92px;height:30px;background:var(--maroon);color:var(--white);font-size:11px;font-weight:700;display:flex;align-items:center;justify-content:center;border-radius:2px}

/* bottom */
.site-footer{left:0;top:2228px;width:1200px;height:272px;background:var(--footer);text-align:center;color:var(--white)}
.footer-brand{position:absolute;left:0;right:0;top:45px;display:flex;flex-direction:column;align-items:center;gap:10px}
.footer-brand .brand-mark{width:46px;height:46px;background:var(--white)}
.footer-brand .brand-name{color:var(--white);font-size:31px}
.copyright{position:absolute;left:0;right:0;top:155px;font-size:10.5px;font-style:italic}
.social{position:absolute;left:420px;top:175px;display:flex;gap:15px}
.social span{width:60px;height:60px;border-radius:50%;background:var(--maroon);display:flex;align-items:center;justify-content:center;font-size:11px;font-weight:700;color:var(--white)}
</style>
</head>
<body>

<header class="site-header abs">
  <div class="brand abs"><span class="brand-mark"></span><span class="brand-name">Munchotronix</span></div>
  <nav class="main-nav abs">
    <a class="active" href="#">Home</a><a href="#">About Us</a><a href="#">Machines</a><a href="#">Request a Machine</a><a href="#">Report a Problem</a><a href="#">Contact Us</a>
  </nav>
</header>

<section class="hero abs" role="img" aria-label="Coffee pouring from a white cup on the left and orange juice splashing around fruit slices on the right, on a dark background"></section>
<div class="hero-splash-left abs"></div>
<div class="hero-splash-right abs"></div>
<div class="hero-caption abs">
  <h1>We Are The Best &nbsp;In Vending Indrusty</h1>
  <p>A Great &nbsp;Selection Of High Quality Vending Machines</p>
</div>
<div class="hero-dots abs"><span></span><span></span><span></span></div>

<article class="category-card abs" style="left:125px">
  <div class="photo" role="img" aria-label="Two women choosing snacks at a vending machine" style="background:linear-gradient(120deg,#3d5a80,#b55a5a 55%,#8a8f9a)"></div>
  <h2>Snacks Vending<br>Machines</h2>
  <span class="read-more">READ MORE <svg viewBox="0 0 12 12"><circle cx="6" cy="6" r="6" fill="#6b2140"/><path d="M5 3.5 7.5 6 5 8.5" stroke="#fff" stroke-width="1.5" fill="none"/></svg></span>
</article>
<div class="category-shadow abs" style="left:125px"></div>

<article class="category-card abs" style="left:450px">
  <div class="photo" role="img" aria-label="Red drinks vending machine beside a wall" style="background:linear-gradient(90deg,#9a8f80,#c0282a 45%,#7a1e20 80%,#bdb6a8)"></div>
  <h2>Drinks Vending<br>Machines</h2>
  <span class="read-more">READ MORE <svg viewBox="0 0 12 12"><circle cx="6" cy="6" r="6" fill="#6b2140"/><path d="M5 3.5 7.5 6 5 8.5" stroke="#fff" stroke-width="1.5" fill="none"/></svg></span>
</article>
<div class="category-shadow abs" style="left:450px"></div>

<article class="category-card abs" style="left:775px">
  <div class="photo" role="img" aria-label="Coffee vending machine filling a paper cup" style="background:linear-gradient(180deg,#1a1a1a,#2a2420 60%,#d8c9a8 80%,#1a1a1a)"></div>
  <h2>Coffee Vending<br>Machines</h2>
  <span class="read-more">READ MORE <svg viewBox="0 0 12 12"><circle cx="6" cy="6" r="6" fill="#6b2140"/><path d="M5 3.5 7.5 6 5 8.5" stroke="#fff" stroke-width="1.5" fill="none"/></svg></span>
</article>
<div class="category-shadow abs" style="left:775px"></div>

<h2 class="about-title abs">About Us</h2>
<div class="about-photo abs" role="img" aria-label="Close-up of snack packets on vending machine shelves"></div>
<div class="about-body abs">
  <h3>Excepteur sint occaecat cupidatat non proident sunt</h3>
  <p>Lorem ipsum dolor sit amet conse ctetur adipisicing elit, sed do eiusmod tempor incididunt ut labore et dolore magna aliqua. Ut enim ad minim veniam, quis nostrud exercitation ullamco laboris nisi ut aliquip ex ea. Duis aute irure dolor in reprehenderit in voluptate velit esse cillum dolore eu fugiat nulla pariatur. Excepteur sint occaecat cupidatat non proident, sunt in culpa. quis nostrud exercitation ullamco laboris nisi ut aliquip ex ea. Duis aute irure dolor in reprehenderit in voluptate velit esse cillum dolore eu fugiat nulla pariatur. Excepteur sint occaecat cupidatat non proident, sunt in culpa</p>
  <span class="btn">READ MORE <svg width="12" height="12" viewBox="0 0 12 12"><circle cx="6" cy="6" r="6" fill="#fff"/><path d="M5 3.5 7.5 6 5 8.5" stroke="#6b2140" stroke-width="1.5" fill="none"/></svg></span>
</div>

<section class="machines-band abs" role="img" aria-label="Faded coffee cup and fruit splash backdrop"></section>

<article class="machine-card abs" style="left:125px">
  <div class="photo"><span role="img" aria-label="Black snack vending machine" style="background:linear-gradient(180deg,#c85040,#d0a040 35%,#1b1b1b 60%)"></span></div>
  <h4>LOREM IPSUM DOLOR SIT</h4>
  <p>Lorem ipsum dolor sit amet conse ctetuav r adipisicing elit, sed do eiusmod tempoev r incididunt ut labore et dolor.Lorem ipszv</p>
  <span class="read-more">READ MORE <svg viewBox="0 0 12 12"><circle cx="6" cy="6" r="6" fill="#6b2140"/><path d="M5 3.5 7.5 6 5 8.5" stroke="#fff" stroke-width="1.5" fill="none"/></svg></span>
</article>
<article class="machine-card abs" style="left:369px">
  <div class="photo"><span role="img" aria-label="Black coffee vending machine with illuminated panel" style="background:linear-gradient(90deg,#3a6ab0,#e0a040 45%,#1b1b1b 65%)"></span></div>
  <h4>LOREM IPSUM DOLOR SIT</h4>
  <p>Lorem ipsum dolor sit amet conse ctetulo r adipisicing elit, sed do eiusmod tempode r incididunt ut labore et dolor.Lorem ipsch</p>
  <span class="read-more">READ MORE <svg viewBox="0 0 12 12"><circle cx="6" cy="6" r="6" fill="#6b2140"/><path d="M5 3.5 7.5 6 5 8.5" stroke="#fff" stroke-width="1.5" fill="none"/></svg></span>
</article>
<article class="machine-card abs" style="left:614px">
  <div class="photo"><span role="img" aria-label="Slim black drinks vending machine with bottle display" style="background:linear-gradient(90deg,#1b1b1b,#3a3a3a 50%,#9aa4b0 75%,#1b1b1b)"></span></div>
  <h4>LOREM IPSUM DOLOR SIT</h4>
  <p>Lorem ipsum dolor sit amet conse ctetuch r adipisicing elit, sed do eiusmod tempotiy r incididunt ut labore et dolor.Lorem ipsee</p>
  <span class="read-more">READ MORE <svg viewBox="0 0 12 12"><circle cx="6" cy="6" r="6" fill="#6b2140"/><path d="M5 3.5 7.5 6 5 8.5" stroke="#fff" stroke-width="1.5" fill="none"/></svg></span>
</article>
<article class="machine-card abs" style="left:858px">
  <div class="photo"><span role="img" aria-label="Stainless drinks dispenser with fruit cocktail artwork" style="background:linear-gradient(180deg,#a8d8f0,#f0a060 40%,#9a9a9a 65%,#6a6a6a)"></span></div>
  <h4>LOREM IPSUM DOLOR SIT</h4>
  <p>Lorem ipsum dolor sit amet conse ctetube r adipisicing elit, sed do eiusmod temponc r incididunt ut labore et dolor.Lorem ipsod</p>
  <span class="read-more">READ MORE <svg viewBox="0 0 12 12"><circle cx="6" cy="6" r="6" fill="#6b2140"/><path d="M5 3.5 7.5 6 5 8.5" stroke="#fff" stroke-width="1.5" fill="none"/></svg></span>
</article>

<section class="newsletter abs">
  <h5>Subscribe To The Newsletter</h5>
  <div class="field">Enter Your Email Address</div>
  <div class="send"><svg width="32" height="28" viewBox="0 0 32 28"><path d="M1 13 31 1 25 27 15 19 27 6 12 17Z" fill="#fff"/><path d="M12 17 14 26 17 20Z" fill="#ddd"/></svg></div>
</section>

<h5 class="col-title abs" style="left:125px">Contact Us</h5>
<ul class="contact-list abs">
  <li><svg viewBox="0 0 16 16"><path d="M8 1a5 5 0 0 0-5 5c0 4 5 9 5 9s5-5 5-9a5 5 0 0 0-5-5Z" fill="#222"/><circle cx="8" cy="6" r="2" fill="#fff"/></svg><span>48 Maple Row, Ottawa Ontario<br>Canada</span></li>
  <li><svg viewBox="0 0 16 16"><path d="M3 1h3l1 4-2 1a9 9 0 0 0 5 5l1-2 4 1v3a2 2 0 0 1-2 2C7 15 1 9 1 3a2 2 0 0 1 2-2Z" fill="#222"/></svg><span style="font-size:16px">hello@munchotronix.example</span></li>
  <li><svg viewBox="0 0 16 16"><rect x="1" y="3" width="14" height="10" fill="none" stroke="#222" stroke-width="1.5"/><path d="M1 3 8 9 15 3" fill="none" stroke="#222" stroke-width="1.5"/></svg><span>+1 (613) 555 0142</span></li>
  <li><svg viewBox="0 0 16 16"><rect x="4" y="1" width="8" height="5" fill="#222"/><rect x="1" y="6" width="14" height="8" fill="#222"/><rect x="4" y="10" width="8" height="5" fill="#fff" stroke="#222"/></svg><span>+1 613-555-0199</span></li>
</ul>

<h5 class="col-title abs" style="left:450px">Information</h5>
<ul class="info-list abs">
  <li><svg viewBox="0 0 12 12"><circle cx="6" cy="6" r="6" fill="#222"/><path d="M5 3.5 7.5 6 5 8.5" stroke="#fff" stroke-width="1.5" fill="none"/></svg>Specials</li>
  <li><svg viewBox="0 0 12 12"><circle cx="6" cy="6" r="6" fill="#222"/><path d="M5 3.5 7.5 6 5 8.5" stroke="#fff" stroke-width="1.5" fill="none"/></svg>New products</li>
  <li><svg viewBox="0 0 12 12"><circle cx="6" cy="6" r="6" fill="#222"/><path d="M5 3.5 7.5 6 5 8.5" stroke="#fff" stroke-width="1.5" fill="none"/></svg>Best sellers</li>
  <li><svg viewBox="0 0 12 12"><circle cx="6" cy="6" r="6" fill="#222"/><path d="M5 3.5 7.5 6 5 8.5" stroke="#fff" stroke-width="1.5" fill="none"/></svg>Our stores</li>
  <li><svg viewBox="0 0 12 12"><circle cx="6" cy="6" r="6" fill="#222"/><path d="M5 3.5 7.5 6 5 8.5" stroke="#fff" stroke-width="1.5" fill="none"/></svg>Contact us</li>
  <li><svg viewBox="0 0 12 12"><circle cx="6" cy="6" r="6" fill="#222"/><path d="M5 3.5 7.5 6 5 8.5" stroke="#fff" stroke-width="1.5" fill="none"/></svg>Pages configuration</li>
  <li><svg viewBox="0 0 12 12"><circle cx="6" cy="6" r="6" fill="#222"/><path d="M5 3.5 7.5 6 5 8.5" stroke="#fff" stroke-width="1.5" fill="none"/></svg>Sitemap</li>
</ul>

<h5 class="col-title abs" style="left:695px">Report a Problem</h5>
<form class="report-form abs">
  <div class="input" style="left:0;top:0;width:186px">First Name</div>
  <div class="input" style="left:195px;top:0;width:185px">Last Name</div>
  <div class="input" style="left:0;top:39px;width:186px">Number</div>
  <div class="input" style="left:195px;top:39px;width:185px">Email Address</div>
  <div class="input" style="left:0;top:78px;width:380px;height:56px">Message</div>
  <div class="submit">SUBMIT</div>
</form>

<footer class="site-footer abs">
  <div class="footer-brand"><span class="brand-mark"></span><span class="brand-name">Munchotronix</span></div>
  <p class="copyright">© copyright 2015 munchotronix. &nbsp;| &nbsp;All Rights Reserved. &nbsp;| &nbsp;Privacy Policy</p>
  <div class="social"><span>Frendo</span><span>Chirpy</span><span>Plusly</span><span>Linkr</span><span>Pinna</span></div>
</footer>

</body>
</html>
```